Velvet Harbor (A luxury Travel Website)

website text attached in document below

images also attached

feel free to use other images if needed

Target Market(s)

Luxury Seekers and wealthy couples / families

Industry/Entity Type

Luxury Travel

Coding

Coded - Design and coding required

Number of Pages Required

1 page

Requirements
Must have
• A luxury design and easy use.
Nice to have
• Ease of use of page, incorporation of images into the flow of the site

```html
<!DOCTYPE html>
<html lang="en">
<head>
<meta charset="utf-8">
<title>Velvet Harbor — Luxury Travel</title>
<link rel="stylesheet" href="https://fonts.googleapis.com/css2?family=Cinzel:wght@400;500&family=Didact+Gothic&family=Mulish:wght@700;800&display=swap">
<style>
:root{
  --navy:#0b3a68;
  --navy-deep:#0a1f3a;
  --ocean:#1f5f98;
  --sky:#3a9ad6;
  --accent:#1b5a94;
  --ink:#1d1d1f;
  --mist:#eaf3fb;
  --white:#ffffff;
  --field-line:#d9dde2;
  --placeholder:#8a8d92;
  --dot:#b9a4a6;
}
*{margin:0;padding:0;box-sizing:border-box}
html,body{width:1200px;height:2203px;overflow:hidden;background:var(--white)}
body{position:relative;font-family:"Didact Gothic",sans-serif;color:var(--ink)}
.abs{position:absolute}

/* hero */
.hero{left:0;top:0;width:1200px;height:620px;overflow:hidden}
.hero-photo{left:0;top:0;width:1200px;height:620px;
  background:linear-gradient(180deg,#0c1b2e 0%,#123a63 22%,#1d5288 45%,#2f6aa3 70%,#3c78ae 100%)}
.hero-wave{left:0;top:430px;width:1200px;height:200px}
.brand{left:0;top:66px;width:1200px;text-align:center;font-family:"Cinzel",serif;font-weight:400;
  font-size:46px;letter-spacing:6px;color:#9fc4e8}
.hero-title{left:0;top:194px;width:1200px;text-align:center;font-family:"Cinzel",serif;font-weight:500;
  font-size:40px;line-height:52px;color:var(--white);letter-spacing:.5px}
.hero-sub{left:0;top:318px;width:1200px;text-align:center;font-size:27px;line-height:34px;color:var(--white)}

/* intro */
.intro{left:0;top:615px;width:1200px;height:362px;
  background:linear-gradient(180deg,#f3f8fd 0%,#e6f0fa 60%,#eef4fb 100%)}
.intro-photo{left:0;top:0;width:600px;height:362px;
  background:linear-gradient(90deg,#6d6e74 0%,#a9abb1 35%,#cfd3d9 70%,rgba(230,240,250,0) 100%)}
.intro-copy{left:641px;top:82px;width:520px;font-size:31px;line-height:41px;color:var(--ink)}
.intro-copy strong{font-family:"Mulish",sans-serif;font-weight:800;color:var(--accent);font-size:30px}
.btn{display:flex;align-items:center;justify-content:center;gap:12px;border:1px solid #2f76b8;border-radius:5px;
  background:linear-gradient(90deg,#6fb0e3 0%,#2f77b7 55%,#1b5a94 100%);color:var(--white);
  font-family:"Mulish",sans-serif;font-weight:800;font-size:16px;letter-spacing:.8px}
.btn-upload{left:641px;top:222px;width:300px;height:51px}

/* enquiry */
.enquiry{left:0;top:977px;width:1200px;height:611px;overflow:hidden}
.enquiry-photo{left:0;top:0;width:1200px;height:611px;
  background:linear-gradient(180deg,#bcd9f1 0%,#dcebf7 35%,#cfe1ef 65%,#bfd6e8 100%)}
.enquiry-figure{left:860px;top:120px;width:340px;height:491px;
  background:linear-gradient(160deg,rgba(160,166,178,.55) 0%,rgba(200,205,222,.45) 60%,rgba(220,228,240,.2) 100%)}
.enquiry-title{left:0;top:66px;width:1200px;text-align:center;font-size:31px;line-height:41px;color:var(--ink);letter-spacing:.4px}
.field{background:var(--white);border:1px solid var(--field-line);color:var(--placeholder);font-size:17px}
.field-name{left:287px;top:188px;width:304px;height:45px;padding:12px 11px}
.field-email{left:621px;top:188px;width:304px;height:45px;padding:12px 27px}
.field-story{left:287px;top:249px;width:638px;height:180px;padding:24px 20px}
.btn-submit{left:509px;top:473px;width:139px;height:51px}

/* gallery */
.gallery{left:0;top:1588px;width:1200px;height:509px;
  background:linear-gradient(180deg,#f7f7f8 0%,#fdfdfd 50%,#f4f4f5 100%)}
.slide{overflow:hidden}
.slide-prev{left:0;top:54px;width:250px;height:320px;background:linear-gradient(135deg,#1ba3b8 0%,#58c4c9 40%,#2f6b45 100%)}
.slide-main{left:274px;top:32px;width:650px;height:364px;background:linear-gradient(180deg,#5a78b4 0%,#3b5a7a 45%,#7a5a3a 65%,#1e4f8a 100%)}
.slide-next{left:949px;top:54px;width:251px;height:320px;background:linear-gradient(135deg,#b88a78 0%,#6b3a34 50%,#3a1d22 100%)}
.arrow{width:60px;height:60px;background:rgba(255,255,255,.8);display:flex;align-items:center;justify-content:center}
.arrow-prev{left:17px;top:158px}
.arrow-next{left:566px;top:158px}
.dots{left:554px;top:440px;display:flex;gap:10px}
.dot{width:10px;height:10px;border-radius:50%;background:var(--dot)}
.dot.is-active{background:var(--accent)}

/* footer */
.footer{left:0;top:2097px;width:1200px;height:106px;background:var(--navy);color:var(--white);
  font-size:12px;text-align:center;line-height:106px;letter-spacing:.3px}
</style>
</head>
<body>

<header class="abs hero">
  <div class="abs hero-photo" role="img" aria-label="Couple relaxing at a candlelit lounge overlooking forested hills at dusk, washed in blue"></div>
  <div class="abs brand">Velvet Harbor</div>
  <h1 class="abs hero-title">LOOKING TO STAY AT A 5 STAR HOTEL<br>OR TO FLY BUSINESS CLASS ANYWHERE?</h1>
  <p class="abs hero-sub">Share a screenshot of your travel plans and<br>we beat the price, within 24 hours</p>
</header>

<section class="abs intro">
  <div class="abs intro-photo" role="img" aria-label="Traveller stepping from a car beside a private jet on the tarmac"></div>
  <p class="abs intro-copy">We work directly with<br>hotels and airlines to get<br>you <strong>the best price,always</strong>.</p>
  <a class="abs btn btn-upload" href="#">
    <svg width="24" height="22" viewBox="0 0 24 22" fill="none" stroke="#fff" stroke-width="1.6">
      <path d="M14 3H2v17h18v-8"/><path d="M2 16l5-5 4 4 3-3 6 6"/><circle cx="7" cy="8" r="1.6"/><path d="M19 1v8M16 6l3 3 3-3"/>
    </svg>
    ADD SCREENSHOOT HERE
  </a>
</section>

<section class="abs enquiry">
  <div class="abs enquiry-photo" role="img" aria-label="Sea view under a bright sky with clouds"></div>
  <div class="abs enquiry-figure" role="img" aria-label="Woman in a striped dress and wide sun hat looking out to sea"></div>
  <h2 class="abs enquiry-title" style="font-weight:400">Tell us about your next holiday plans.<br>The more details the better</h2>
  <div class="abs field field-name">Your full name</div>
  <div class="abs field field-email">Your email</div>
  <div class="abs field field-story">Tell your travel story here</div>
  <a class="abs btn btn-submit" href="#">SUBMIT</a>
</section>

<section class="abs gallery">
  <div class="abs slide slide-prev" role="img" aria-label="Aerial view of a tropical island with overwater villas"></div>
  <div class="abs slide slide-main" role="img" aria-label="Resort with palm trees and an infinity pool lit at dusk">
    <span class="abs arrow arrow-prev"><svg width="30" height="24" viewBox="0 0 30 24" fill="none" stroke="#111" stroke-width="2.4"><path d="M28 12H3M13 2L3 12l10 10"/></svg></span>
    <span class="abs arrow arrow-next"><svg width="30" height="24" viewBox="0 0 30 24" fill="none" stroke="#111" stroke-width="2.4"><path d="M2 12h25M17 2l10 10-10 10"/></svg></span>
  </div>
  <div class="abs slide slide-next" role="img" aria-label="Passenger relaxing in a business class seat"></div>
  <div class="abs dots">
    <span class="dot"></span><span class="dot is-active"></span><span class="dot"></span><span class="dot"></span><span class="dot"></span>
  </div>
</section>

<svg class="abs hero-wave" style="top:430px" width="1200" height="200" viewBox="0 0 1200 200" aria-hidden="true">
  <defs>
    <linearGradient id="waveBand" x1="0" x2="1">
      <stop offset="0" stop-color="#3fa3dd"/><stop offset=".55" stop-color="#1b5f9c"/><stop offset="1" stop-color="#1a5a96"/>
    </linearGradient>
  </defs>
  <path d="M0 70 C120 0 330 20 560 90 C800 160 1050 200 1200 100 L1200 200 L0 200 Z" fill="url(#waveBand)"/>
  <path d="M0 80 C130 20 330 38 560 104 C800 172 1060 205 1200 116 L1200 200 L0 200 Z" fill="#f4f9fd"/>
</svg>

<footer class="abs footer">©2022 VELVET HARBOR.COM.AU</footer>

</body>
</html>
```